Ecommerce web site design for 80s Retro website

we need a website to sell retro gift boxes based around 80's movies, music and gaming
it needs to work with the cartvella ecommerce provider
there would only be 3 basic gift boxes (music, movies and gaming) , but the packaging would be able to be chosen to match birthdays, Christmas etc.
Each themed box will also have three levels of pricing, classic, premium, ultimate.
the website should be themed around the same colour scheme and look as the logo.

Target Market(s)

People after retro presents and gifts so probably people in their 40s to 50s

Coding

Coded - Design and coding required

Number of Pages Required

1 page

Requirements
Must have
• A real retro look and feel with bright neon colours and some icons or symbols of things from the 80s like walkmans, joysticks, movies, music, gaming etc
Should not have
• A boring bland interface

```html
<!DOCTYPE html>
<html lang="en">
<head>
<meta charset="utf-8">
<title>Neon Attic – 80s Gift Boxes</title>
<link href="https://fonts.googleapis.com/css2?family=Open+Sans:wght@400;600;700&family=Russo+One&display=swap" rel="stylesheet">
<style>
:root{
  --blue:#1a73c8;
  --pink:#e2007a;
  --sky:#1fa2e6;
  --purple:#4b2ad1;
  --ink:#1d1d1d;
  --muted:#555;
  --line:#cfcfcf;
  --link:#1a73c8;
}
*{margin:0;padding:0;box-sizing:border-box}
html,body{width:1200px;height:2518px;overflow:hidden;background:#fff}
body{position:relative;font-family:"Open Sans",Arial,sans-serif;color:var(--ink)}
.abs{position:absolute}
.promo-bar{left:0;top:0;width:1200px;height:53px;background:var(--blue);color:#fff;font-size:15px}
.promo-bar .msg{left:144px;top:15px}
.promo-bar .bell{left:110px;top:14px}
.promo-bar .close{left:1070px;top:16px}
.util-bar{left:0;top:53px;width:1200px;height:64px;background:var(--pink);color:#fff;font-size:15px}
.util-bar .left{left:110px;top:22px}
.util-bar .right{left:624px;top:22px}
.util-bar .total{left:862px;top:20px;font-weight:700;font-size:17px}
.checkout{left:930px;top:7px;width:158px;height:50px;background:var(--sky);border-radius:4px;color:#fff;font-size:17px;text-align:center;line-height:50px}
.brand{left:111px;top:150px;display:flex;align-items:center;gap:10px}
.brand .dot{width:22px;height:22px;background:var(--pink)}
.brand span{font-size:26px;font-weight:700;color:var(--purple)}
.region{left:905px;top:135px;font-size:16px;display:flex;align-items:center;gap:8px;font-weight:600;color:#333}
.region .flag{width:26px;height:26px;border-radius:50%;background:linear-gradient(#c8102e 0 50%,#f2f2f2 50%)}
.search{left:985px;top:177px;font-size:16px;color:#333}
.main-nav{left:438px;top:214px;display:flex;gap:31px;font-size:16px;color:#222}
.hero{left:111px;top:255px;width:977px;height:617px;background:radial-gradient(circle at 55% 40%,#f2b27a,#c36a3b 45%,#6e3219 90%)}
.hero-caption{left:111px;top:704px;width:707px;height:74px;background:rgba(20,20,20,.88)}
.hero-caption h1{position:absolute;left:27px;top:20px;font-family:"Russo One",sans-serif;font-size:26px;font-weight:400;color:#7b2ff2;white-space:nowrap}
.section-title{font-family:"Russo One",sans-serif;font-weight:400;font-size:36px;background:linear-gradient(90deg,var(--purple),var(--pink));-webkit-background-clip:text;background-clip:text;color:transparent;text-align:center;width:1200px;left:0}
.sub{left:0;width:1200px;text-align:center;top:978px;font-size:17px;color:#333}
.tier{width:304px}
.tier .pic{height:383px}
.tier h3{margin-top:24px;font-size:20px;font-weight:400;letter-spacing:.5px}
.tier a{display:block;margin-top:12px;color:var(--link);font-size:17px;text-decoration:none}
.rule{height:1px;background:var(--line)}
.product{width:228px;top:1736px}
.product .pic{height:307px;position:relative}
.product .meta{display:flex;justify-content:space-between;margin-top:24px;font-size:17px;line-height:27px}
.badge{position:absolute;bottom:0;width:73px;height:52px;background:var(--pink);display:flex;align-items:center;justify-content:center}
.arrow{top:1873px}
.foot-col h4{font-size:17px;font-weight:600;letter-spacing:.3px;margin-bottom:12px}
.foot-col p{font-size:17px;line-height:26px;color:#333}
.email{left:608px;top:2279px;width:258px;height:59px;border:1px solid #bbb;font-size:17px;padding:19px 20px;color:#333}
.social{top:2355px;width:31px;height:31px}
.copy{left:111px;top:2486px;font-size:17px;color:#333}
.pay{left:790px;top:2478px;width:302px;height:36px;background:#f1f1f1;display:flex;gap:6px;align-items:center;padding:0 8px}
.pay i{display:block;width:26px;height:18px;background:#c9c9c9;border-radius:2px}
</style>
</head>
<body>

<div class="abs promo-bar">
  <svg class="abs bell" width="22" height="24" viewBox="0 0 22 24"><path d="M11 2c-4 0-7 3-7 7v6l-3 4h20l-3-4V9c0-4-3-7-7-7z" fill="#fff"/><circle cx="11" cy="21" r="3" fill="#fff"/></svg>
  <div class="abs msg">Use code FLASH20 at checkout for an additional 20% off your order</div>
  <svg class="abs close" width="18" height="18" viewBox="0 0 18 18"><path d="M3 3l12 12M15 3L3 15" stroke="#fff" stroke-width="3"/></svg>
</div>

<div class="abs util-bar">
  <div class="abs left">HOME &nbsp;// &nbsp;CONTACT US</div>
  <div class="abs right">YOUR ACCOUNT &nbsp;// &nbsp;WISH LIST</div>
  <div class="abs total">$0.00</div>
  <div class="abs checkout">CHECK OUT</div>
</div>

<div class="abs brand"><div class="dot"></div><span>Neon Attic</span></div>
<div class="abs region"><div class="flag"></div>United States($)
  <svg width="12" height="8" viewBox="0 0 12 8"><path d="M1 1l5 5 5-5" stroke="#333" fill="none" stroke-width="1.5"/></svg></div>
<div class="abs search">Search... &nbsp;
  <svg width="22" height="22" viewBox="0 0 22 22" style="vertical-align:middle"><circle cx="9" cy="9" r="7" stroke="#111" stroke-width="2" fill="none"/><path d="M14 14l6 6" stroke="#111" stroke-width="2.5"/></svg></div>
<nav class="abs main-nav"><span>MUSIC</span><span>GAMES</span><span>MOVIES</span><span>GIFTS</span><span>NEW SALE</span><span>GIFT VOUCHER</span><span>BLOG</span></nav>

<div class="abs hero" role="img" aria-label="Close-up photo of a warm-lit vintage carousel music box"></div>
<div class="abs hero-caption"><h1>NEON ATTIC FOR 80’S MUSIC, MOVIE AND GAMES</h1></div>

<h2 class="abs section-title" style="top:922px">OUR PRICING</h2>
<p class="abs sub">Duis aute irure dolor in reprehenderit in voluptate velit esse cillum.</p>

<div class="abs tier" style="left:111px;top:1051px">
  <div class="pic" role="img" aria-label="Open jewellery music box with a small dancer" style="background:linear-gradient(160deg,#4a2414,#2c6a6a 40%,#7a3a1c 80%)"></div>
  <h3>CLASSIC</h3><a href="#">SHOP NOW &nbsp;›</a>
</div>
<div class="abs tier" style="left:448px;top:1051px">
  <div class="pic" role="img" aria-label="Colourful retro board game box" style="background:linear-gradient(135deg,#e9e2d8,#d7d1c6 45%,#b55ab0 70%,#4d9ed6)"></div>
  <h3>PREMIUM</h3><a href="#">SHOP NOW &nbsp;›</a>
</div>
<div class="abs tier" style="left:785px;top:1051px">
  <div class="pic" role="img" aria-label="Film clapperboard and movie reel on blue backdrop" style="background:radial-gradient(circle at 50% 30%,#3aa7ea,#0b3c7a 80%)"></div>
  <h3>ULTIMATE</h3><a href="#">SHOP NOW &nbsp;›</a>
</div>

<div class="abs rule" style="left:111px;top:1639px;width:280px"></div>
<div class="abs rule" style="left:809px;top:1639px;width:279px"></div>
<h2 class="abs section-title" style="top:1614px">FEATURED PRODUCTS</h2>

<svg class="abs arrow" style="left:44px" width="20" height="34" viewBox="0 0 20 34"><path d="M17 2L3 17l14 15" stroke="#777" stroke-width="2" fill="none"/></svg>
<svg class="abs arrow" style="left:1133px" width="20" height="34" viewBox="0 0 20 34"><path d="M3 2l14 15L3 32" stroke="#111" stroke-width="2" fill="none"/></svg>

<div class="abs product" style="left:111px">
  <div class="pic" role="img" aria-label="Small painted hand-crank music box" style="background:radial-gradient(circle at 50% 50%,#6cbbe0,#e6e8ea 55%)"></div>
  <div class="meta"><span>MUSIC BOX<br>GIFT</span><span>$100</span></div>
</div>
<div class="abs product" style="left:361px">
  <div class="pic" role="img" aria-label="Clapperboard and film reel in grey tones" style="background:radial-gradient(circle at 55% 45%,#8a8a8a,#e9e9e9 65%)">
    <div class="badge" style="left:0"><svg width="34" height="32" viewBox="0 0 34 32"><path d="M17 1l4.5 10 11 1-8.3 7.4 2.5 11L17 24.7 7.3 30.4l2.5-11L1.5 12l11-1z" fill="#fff"/></svg></div>
    <div class="badge" style="right:0"><svg width="40" height="26" viewBox="0 0 40 26"><path d="M2 13C8 4 32 4 38 13 32 22 8 22 2 13z" fill="none" stroke="#fff" stroke-width="3"/><circle cx="20" cy="13" r="5" fill="#fff"/></svg></div>
  </div>
  <div class="meta"><span>MOVIE BOX<br>GIFT</span><span>$100</span></div>
</div>
<div class="abs product" style="left:611px">
  <div class="pic" role="img" aria-label="Boxed retro games console" style="background:radial-gradient(circle at 50% 50%,#2b5f9e,#dfe3e8 70%)"></div>
  <div class="meta"><span>GAME BOX<br>GIFT</span><span>$100</span></div>
</div>
<div class="abs product" style="left:860px">
  <div class="pic" role="img" aria-label="White and blue carousel music box" style="background:radial-gradient(circle at 50% 50%,#bcd2e6,#dcdcdc 60%,#8f8f8f)"></div>
  <div class="meta"><span>MUSIC BOX<br>GIFT</span><span>$100</span></div>
</div>

<div class="abs rule" style="left:111px;top:2197px;width:977px"></div>

<div class="abs foot-col" style="left:111px;top:2241px"><h4>ABOUT US</h4><p>About Us<br>My Account<br>Create Account</p></div>
<div class="abs foot-col" style="left:319px;top:2241px"><h4>CUSTOMER INFORMATION</h4><p>Frequently Asked Questions<br>Contact Us<br>Privacy Policy<br>Terms &amp; Conditions<br>Delivery Information<br>Refunds &amp; Returns</p></div>
<div class="abs foot-col" style="left:608px;top:2241px"><h4>CONNECT WITH US</h4></div>
<div class="abs email">Email ID
  <svg style="position:absolute;right:24px;top:22px" width="10" height="16" viewBox="0 0 10 16"><path d="M2 2l6 6-6 6" stroke="#333" stroke-width="1.5" fill="none"/></svg></div>
<div class="abs social" style="left:610px;background:#3b5bab"></div>
<div class="abs social" style="left:649px;background:#1fa2e6"></div>
<div class="abs social" style="left:688px;background:#1a6fb0"></div>
<div class="abs social" style="left:727px;background:#d0202f"></div>
<div class="abs social" style="left:766px;background:#e01b1b"></div>
<div class="abs social" style="left:610px;top:2394px;background:#6b4a3a"></div>
<div class="abs foot-col" style="left:917px;top:2241px"><h4>GET IN TOUCH</h4><p>Neon Attic,<br>Address comes here</p><p style="margin-top:8px">T: +1 555-014-2200<br>E: hello@neonattic.shop</p></div>

<div class="abs rule" style="left:111px;top:2462px;width:977px"></div>
<div class="abs copy">Copyright © 2022 Neon Attic. All Rights Reserved.</div>
<div class="abs pay" role="img" aria-label="Accepted payment methods"><i></i><i></i><i></i><i></i><i></i><i></i><i></i><i></i><i></i></div>

</body>
</html>
```